I want to create a postcard we can use as a promotional offer. We may send out to prospects or give to people at an event to get them in front of us and start to understand their business more with the hope of engaging them as clients eventually.
The offer is a Complimentary "Venture Spark Kit". (valued at $875)
The kit includes:
Fiscal Horizon Audit
45 minute Business Discovery Meeting
6 point Diagnostic Report
3 Recommendations for your Business

The headline and there look and feel we would like the design to be focused upon is "Analyze. Boost. Grow."
Include an Image(s) as you feel appropriate.
I'm thinking Headline/Mian Branding and Picture on the Front, then Offer and details of Kit and Logos etc on the Back.

Include 2 logos as we are part of a joint operation, Meridale Accountants & Trovenly.

Call to action to Phone 0255501872 or email hello@trovenly.com.au

Logo's uploaded, committed payment, increased deadline.

Target Market(s)

Small to Medium Business

Industry/Entity Type

Business

Requirements
Must have
• Logos in Colour on Back with rest of Detail.
Front to be all about the key message "Analyze. Boost. Grow." select pic to represent.
Must create cut through and intrigue to make the holder tunr the card and read.

```html
<!DOCTYPE html>
<html lang="en">
<head>
<meta charset="utf-8">
<title>Venture Spark Kit Postcard</title>
<link rel="stylesheet" href="https://fonts.googleapis.com/css2?family=Open+Sans:wght@400;600&family=PT+Sans+Narrow:wght@400;700&family=Marcellus&display=swap">
<style>
  :root {
    --stage-green: #84c441;
    --card-black: #0b0f11;
    --navy: #1d3d63;
    --brand-blue: #2a6e9a;
    --sky: #3fa9d9;
    --leaf: #5a9e3a;
    --leaf-bright: #8cc63f;
    --ink: #1c1c1c;
    --offer-red: #d0242b;
    --stamp: #f4f4f4;
    --chalk-light: #5a5c5b;
    --chalk-mid: #383a3a;
    --chalk-dark: #1d2021;
  }
  * { margin: 0; padding: 0; box-sizing: border-box; }
  html, body { width: 1200px; height: 1000px; overflow: hidden; }
  body { background: var(--stage-green); position: relative; font-family: "Open Sans", Arial, sans-serif; }

  .card { position: absolute; }

  /* Back of postcard */
  .card-back {
    left: 83px; top: 98px; width: 672px; height: 522px;
    background: linear-gradient(135deg, #ffffff 0%, #f5f8f2 45%, #ffffff 100%);
  }
  .stamp-box { position: absolute; left: 522px; top: 30px; width: 115px; height: 123px; background: var(--stamp); }

  .partner { position: absolute; display: flex; align-items: center; gap: 8px; }
  .partner-trovenly { left: 44px; top: 64px; }
  .partner-meridale { left: 250px; top: 64px; }
  .partner-mark { width: 22px; height: 22px; }
  .partner-mark.circle { border-radius: 50%; background: var(--leaf); }
  .partner-mark.square { background: var(--navy); }
  .partner-name { font-family: "PT Sans Narrow", sans-serif; font-weight: 700; font-size: 26px; }
  .partner-trovenly .partner-name { color: var(--leaf); }
  .partner-meridale .partner-name { color: var(--navy); }

  .kit-badge { position: absolute; left: 27px; top: 133px; width: 98px; height: 98px; }
  .kit-title { position: absolute; left: 130px; top: 145px; text-align: center; font-family: "PT Sans Narrow", sans-serif; }
  .kit-title .eyebrow { color: var(--sky); font-size: 21px; line-height: 26px; }
  .kit-title .name { color: var(--navy); font-weight: 700; font-size: 28px; line-height: 32px; }
  .kit-title .value { color: var(--leaf); font-weight: 700; font-size: 20px; line-height: 28px; }

  .kit-contents { position: absolute; left: 33px; top: 244px; list-style: none; font-size: 15px; line-height: 25px; color: var(--ink); }
  .kit-contents strong { font-weight: 600; }
  .kit-contents .blue { color: var(--brand-blue); }
  .kit-contents .green { color: var(--leaf); }

  .call-to-action { position: absolute; left: 33px; top: 354px; font-family: "PT Sans Narrow", sans-serif; font-weight: 700; font-size: 18px; line-height: 25px; color: var(--brand-blue); }

  /* Front of postcard */
  .card-front {
    left: 461px; top: 378px; width: 686px; height: 532px;
    background: var(--card-black); overflow: hidden;
  }
  .hero-photo {
    position: absolute; left: 100px; top: 20px; width: 586px; height: 512px;
    background:
      radial-gradient(ellipse 120px 150px at 58% 82%, rgba(225,228,230,0.55) 0%, rgba(225,228,230,0) 100%),
      radial-gradient(ellipse 70% 60% at 50% 38%, var(--chalk-light) 0%, var(--chalk-mid) 45%, var(--chalk-dark) 75%, rgba(11,15,17,0) 100%),
      linear-gradient(90deg, rgba(11,15,17,1) 0%, rgba(11,15,17,0) 18%, rgba(11,15,17,0) 82%, rgba(11,15,17,0.6) 100%);
  }
  .headline {
    position: absolute; top: 62px; width: 100%; text-align: center;
    font-family: "Marcellus", Georgia, serif; font-weight: 400; font-size: 40px; color: #ffffff; letter-spacing: 0.5px;
  }
  .headline .analyze { color: var(--leaf-bright); }
  .headline .grow { color: var(--sky); }
  .front-badge { position: absolute; left: 291px; top: 121px; width: 104px; height: 104px; }
  .front-offer { position: absolute; top: 404px; width: 100%; text-align: center; }
  .front-offer .kit-name { font-family: "PT Sans Narrow", sans-serif; font-weight: 700; font-size: 63px; line-height: 64px; color: var(--leaf-bright); }
  .front-offer .terms { margin-top: 2px; font-size: 15px; color: #ffffff; }
  .front-offer .free { font-family: "PT Sans Narrow", sans-serif; font-weight: 700; font-size: 21px; color: var(--offer-red); margin-right: 10px; }
</style>
</head>
<body>

<section class="card card-back">
  <div class="stamp-box"></div>

  <div class="partner partner-trovenly">
    <span class="partner-mark circle"></span>
    <span class="partner-name">Trovenly</span>
  </div>
  <div class="partner partner-meridale">
    <span class="partner-mark square"></span>
    <span class="partner-name">Meridale Accountants</span>
  </div>

  <svg class="kit-badge" viewBox="0 0 100 100" aria-hidden="true">
    <circle cx="50" cy="50" r="48" fill="#e9eef2"/>
    <circle cx="50" cy="50" r="42" fill="#2a6e9a"/>
  </svg>

  <div class="kit-title">
    <p class="eyebrow">Complimentary</p>
    <p class="name">Venture Spark Kit</p>
    <p class="value">(valued at $875)</p>
  </div>

  <ul class="kit-contents">
    <li>Fiscal <strong class="blue">Horizon Audit</strong></li>
    <li><strong class="green">45 minute</strong> Business Discovery Meeting</li>
    <li><strong class="blue">6 point</strong> Diagnostic Report</li>
    <li><strong class="green">3 Recommendations</strong> for your Business</li>
  </ul>

  <p class="call-to-action">Call to action to Phone 0255501872<br>or email hello@trovenly.com.au</p>
</section>

<section class="card card-front">
  <div class="hero-photo" role="img" aria-label="Photo of a businessman in glasses and a white shirt reaching up to pull a light bulb cord, in front of a dark chalkboard sketched with business icons, bar charts, a puzzle piece, a target and the words problems, solutions and think outside the box"></div>

  <h1 class="headline"><span class="analyze">Analyze</span>. Boost. <span class="grow">Grow</span>.</h1>

  <svg class="front-badge" viewBox="0 0 100 100" aria-hidden="true">
    <circle cx="50" cy="50" r="48" fill="#ffffff"/>
    <circle cx="50" cy="50" r="43" fill="#2a6e9a"/>
  </svg>

  <div class="front-offer">
    <p class="kit-name">"Venture Spark Kit"</p>
    <p class="terms"><span class="free">Free Offer</span>(valued at $875)</p>
  </div>
</section>

</body>
</html>
```